Creative label for amber glass candle jar.

We are a candle company. Our products are handmade by us and natural. We are looking for something minimalistic and unique. We need a label for our candle jars (amber glass with black lid). Our current label doesn't match these requirements. We would like our products to be stocked in London shop, therefore design has to be up to a high standard. Jar specification Diameter (mm) 65 Height without cap (mm) 80. We want the new design to be different from the current one. It's just a guide for wording.
We should be able adjust the label, to change scent name.
Our scents are
*Coconut & Vanilla
*Lavender
*Bergamot
*Italian Garden
*Hygge
*Eucalyptus & Peppermint
*Coffee
*Cedarwood & Juniperberry
To know more about us, visit our website www.fenwickbrae.com or instagram.com/fenwickbrae
Good luck!
Industry/Entity Type
It Company
Colors
Designer to choose colors to be used in the design.
Requirements
Must have
- * I have attached two of our logos, label design must include one of them.
- *has to mention that it's made in London
- *has to say that candle is natural/made with essential oils
- *has to have scent name and No. on it..
- Label can be vertical or horizontal, but has to be square/rectangular,.
Should not have
- Label should not be round

```html
<!DOCTYPE html>
<html lang="en">
<head>
<meta charset="utf-8">
<title>olvra – candle label redesign</title>
<link rel="stylesheet" href="https://fonts.googleapis.com/css2?family=Share+Tech+Mono&display=swap">
<style>
  :root {
    --ink: #0d0b0a;
    --paper: #dcc3a8;
    --paper-edge: #d2b699;
    --backdrop-warm: #d9c6b8;
    --backdrop-rose: #d79a9c;
    --backdrop-grey: #a9a3a0;
    --backdrop-light: #e7e2de;
  }
  * { margin: 0; padding: 0; box-sizing: border-box; }
  html, body { width: 767px; height: 1200px; overflow: hidden; }
  body {
    position: relative;
    font-family: "Share Tech Mono", monospace;
    font-weight: 400;
    color: var(--ink);
    background: var(--backdrop-light);
  }
  h1, h2, p { font-weight: 400; }
  .backdrop {
    position: absolute; inset: 0;
    background:
      radial-gradient(ellipse 240px 160px at 150px 90px, var(--backdrop-rose), transparent 70%),
      radial-gradient(ellipse 520px 160px at 420px 520px, var(--backdrop-grey), transparent 75%),
      radial-gradient(ellipse 520px 140px at 420px 720px, var(--backdrop-grey), transparent 75%),
      linear-gradient(180deg, var(--backdrop-warm) 0%, #cfc3bb 45%, var(--backdrop-light) 100%);
  }
  .board-brand {
    position: absolute; left: 59px; top: 38px;
    font-size: 80px; line-height: 1; letter-spacing: 4px;
  }
  .board-subtitle {
    position: absolute; left: 133px; top: 131px;
    font-size: 24px; line-height: 1.2; letter-spacing: 1px;
  }
  .board-version {
    position: absolute; left: 62px; top: 195px;
    font-size: 24px; line-height: 1.2; letter-spacing: 1px;
  }
  .label {
    position: absolute; width: 300px; height: 424px;
    background: linear-gradient(160deg, var(--paper) 0%, var(--paper-edge) 100%);
    text-align: center;
  }
  .label-brand {
    position: absolute; left: 0; right: 0; top: 44px;
    font-size: 68px; line-height: 1; letter-spacing: 3px;
  }
  .label-number {
    position: absolute; left: 0; right: 0; top: 202px;
    font-size: 18px; line-height: 1.2;
  }
  .label-scent {
    position: absolute; left: 0; right: 0; top: 236px;
    font-size: 23px; line-height: 1.25; letter-spacing: 1px;
  }
  .label-tagline {
    position: absolute; left: 0; right: 0; top: 305px;
    font-size: 15px; line-height: 1.22;
  }
  .col-1 { left: 63px; }
  .col-2 { left: 407px; }
  .row-1 { top: 267px; }
  .row-2 { top: 735px; }
</style>
</head>
<body>
  <div class="backdrop" role="img" aria-label="Softly blurred photograph of a candle setting in warm beige, rose and grey tones"></div>

  <header>
    <h1 class="board-brand">olvra</h1>
    <p class="board-subtitle">candle label redesign</p>
    <p class="board-version">design 01</p>
  </header>

  <main>
    <article class="label col-1 row-1">
      <div class="label-brand">olvra</div>
      <p class="label-number">08</p>
      <h2 class="label-scent">cedarwood &amp;<br>juniperberry</h2>
      <p class="label-tagline">handpoured in london<br>made from natural<br>essential oils</p>
    </article>

    <article class="label col-2 row-1">
      <div class="label-brand">olvra</div>
      <p class="label-number">01</p>
      <h2 class="label-scent">coconut &amp;<br>vanilla</h2>
      <p class="label-tagline">handpoured in london<br>made from natural<br>essential oils</p>
    </article>

    <article class="label col-1 row-2">
      <div class="label-brand">olvra</div>
      <p class="label-number">02</p>
      <h2 class="label-scent">lavender</h2>
      <p class="label-tagline">handpoured in london<br>made from natural<br>essential oils</p>
    </article>

    <article class="label col-2 row-2">
      <div class="label-brand">olvra</div>
      <p class="label-number">03</p>
      <h2 class="label-scent">bergamot</h2>
      <p class="label-tagline">handpoured in london<br>made from natural<br>essential oils</p>
    </article>
  </main>
</body>
</html>
```